Reel Courier - Online Lab - Send Huge Files - Edit HD Masters - Online Screening

We need new amazing web design for a new web-solution. It´s like an online movie lab. Where you can send huge movie file masters (120-250 GB), edit them, screen them, convert and transcode. The name is www.reelcourier.net and logo is attached. Attached is also screenshots of how the site looks today. Pretty basic design. We need it to be more attractive.

Target Market(s)

Film distributors and producers

Industry/Entity Type

Movie

Number of Pages Required

1 page

Font styles to use
Serif

Requirements
Must have
• Dark background

```html
<!DOCTYPE html>
<html lang="en">
<head>
<meta charset="utf-8">
<title>Reel Courier – Online Movie Lab</title>
<link href="https://fonts.googleapis.com/css2?family=Playfair+Display:wght@400;500&family=Lora:wght@400;500&display=swap" rel="stylesheet">
<style>
  :root {
    --orange: #f7741f;
    --accent-blue: #6fb3e8;
    --heading: #f2f2f2;
    --body: #b9bec6;
    --ink: #e4e6ea;
    --page: #14171c;
    --header: #0f1115;
    --hero-bg: #0f1d26;
    --panel: #1b1f26;
    --footer: #0b0c0f;
    --white: #ffffff;
  }
  * { margin: 0; padding: 0; box-sizing: border-box; }
  html, body { width: 870px; height: 1200px; overflow: hidden; }
  body { position: relative; background: var(--page); font-family: "Lora", Georgia, serif; color: var(--body); }
  .abs { position: absolute; }
  a { text-decoration: none; }

  .site-header { left: 0; top: 0; width: 870px; height: 71px; background: var(--header); box-shadow: 0 1px 3px rgba(0,0,0,.4); z-index: 2; }
  .brand { left: 55px; top: 22px; display: flex; align-items: center; gap: 7px; }
  .brand-mark { width: 18px; height: 18px; background: var(--orange); }
  .brand-name { font-family: "Playfair Display", serif; font-weight: 500; font-size: 19px; color: var(--heading); }
  .main-nav { left: 454px; top: 38px; display: flex; align-items: center; font-size: 11px; color: var(--ink); }
  .main-nav a { color: inherit; display: block; height: 22px; line-height: 22px; }
  .main-nav .active { background: var(--orange); color: var(--white); width: 55px; text-align: center; margin-right: 20px; }
  .main-nav .n-about { margin-right: 28px; }
  .main-nav .n-services { margin-right: 33px; }
  .main-nav .n-blog { margin-right: 35px; }
  .main-nav .n-gallery { margin-right: 27px; }

  .hero { left: 0; top: 71px; width: 870px; height: 353px; background: var(--hero-bg); overflow: hidden; }
  .hero-title { left: 94px; top: 94px; font-family: "Playfair Display", serif; font-weight: 400; font-size: 25px; line-height: 33px; color: var(--accent-blue); letter-spacing: .5px; }
  .hero-text { left: 96px; top: 174px; width: 262px; font-size: 11.5px; line-height: 20px; color: var(--ink); text-align: justify; }
  .hero-dots { left: 95px; top: 246px; display: flex; gap: 4px; }
  .hero-dots span { width: 8px; height: 8px; border-radius: 50%; background: #3d5663; }
  .hero-dots span:first-child { background: var(--orange); }
  .hero-visual { left: 430px; top: 30px; width: 440px; height: 323px; background: radial-gradient(ellipse 55% 60% at 68% 48%, #1a2430 0%, #2b5567 40%, #3f8ea3 60%, rgba(15,29,38,0) 80%); }
  .hero-shadow { left: 50px; top: 424px; width: 770px; height: 8px; background: radial-gradient(ellipse at 50% 0, rgba(0,0,0,.8), rgba(0,0,0,0) 70%); }

  .section-title { width: 870px; left: 0; text-align: center; font-family: "Playfair Display", serif; font-weight: 400; font-size: 22px; color: var(--heading); }
  .section-title .accent { color: var(--orange); }
  .welcome-title { top: 462px; }
  .welcome-text { left: 65px; top: 500px; width: 740px; font-size: 8.6px; line-height: 16px; text-align: center; }
  .btn { display: block; background: var(--orange); color: var(--white); font-family: "Lora", serif; font-weight: 500; font-size: 10px; text-align: center; line-height: 25px; height: 25px; }
  .welcome-btn { left: 391px; top: 562px; width: 87px; }

  .services { left: 0; top: 611px; width: 870px; height: 266px; background: var(--panel); }
  .services-title { top: 36px; }
  .service { width: 240px; text-align: center; top: 68px; }
  .service .icon-disc { width: 80px; height: 80px; margin: 0 auto; border-radius: 50%; background: #2a2f38; display: flex; align-items: center; justify-content: center; }
  .service .icon-art { width: 40px; height: 40px; border-radius: 4px; background: linear-gradient(135deg, #3ba7d6, #f6c33a); }
  .service h3 { margin-top: 14px; font-family: "Playfair Display", serif; font-weight: 400; font-size: 12px; color: var(--orange); letter-spacing: .3px; }
  .service p { margin-top: 6px; font-size: 8.8px; line-height: 16px; text-align: justify; text-align-last: center; padding: 0 6px; }

  .interface-title { top: 910px; }
  .interface-heading { left: 54px; top: 958px; font-family: "Playfair Display", serif; font-weight: 400; font-size: 12px; color: var(--accent-blue); letter-spacing: .3px; }
  .interface-text { left: 54px; top: 983px; width: 307px; font-size: 8.8px; line-height: 16px; text-align: justify; }
  .interface-btn { left: 55px; top: 1060px; width: 86px; }
  .screen { border: 1px solid #333a44; box-shadow: 0 1px 4px rgba(0,0,0,.5); }
  .screen-media { left: 388px; top: 957px; width: 202px; height: 128px; background: linear-gradient(#2d2d2d 0 10px, #f4f4f4 10px); }
  .screen-player { left: 614px; top: 957px; width: 202px; height: 118px; background: linear-gradient(90deg, #eeeeee 0 34px, #5c6b4a 34px 164px, #eeeeee 164px); }

  .site-footer { left: 0; top: 1133px; width: 870px; height: 67px; background: var(--footer); }
  .copyright { left: 55px; top: 30px; font-size: 9px; color: var(--ink); }
  .social { left: 700px; top: 24px; display: flex; gap: 4px; }
  .social span { width: 20px; height: 20px; border-radius: 50%; background: var(--white); }
</style>
</head>
<body>
  <header class="site-header abs">
    <div class="brand abs"><span class="brand-mark"></span><span class="brand-name">Reel Courier</span></div>
    <nav class="main-nav abs">
      <a class="active" href="#">Home</a>
      <a class="n-about" href="#">About</a>
      <a class="n-services" href="#">Services</a>
      <a class="n-blog" href="#">Blog</a>
      <a class="n-gallery" href="#">Gallery</a>
      <a href="#">Contact</a>
    </nav>
  </header>

  <section class="hero abs">
    <h1 class="hero-title abs">WE ARE AN<br>ONLINE MOVIE LAB</h1>
    <p class="hero-text abs">Where you can send huge movie file masters (120-250 GB), edit them, screen them, convert and transcode.</p>
    <div class="hero-dots abs"><span></span><span></span><span></span><span></span></div>
    <div class="hero-visual abs" role="img" aria-label="Film reel with loose strips of movie film"></div>
  </section>
  <div class="hero-shadow abs"></div>

  <h2 class="section-title welcome-title abs">Welcome to Our <span class="accent">Site</span></h2>
  <p class="welcome-text abs">Lorem ipsum dolor sit amet, consectetur adipiscing elit, sed do eiusmod tempor incididunt ut labore et dolore magna aliqua. Ut enim ad minim veniam, quis nostrud exercitation ullamco laboris nisi ut aliquip ex ea commodo consequat. Lorem ipsum dolor sit amet, consectetur adipiscing elit, sed do eiusmod tempor incididunt ut labore et dolore magna aliqua. Ut enim ad minim veniam, quis nostrud exercitation ullamco laboris nisi ut aliquip ex ea commodo consequat.</p>
  <a class="btn welcome-btn abs" href="#">Learn More</a>

  <section class="services abs">
    <h2 class="section-title services-title abs">Our Services</h2>
    <div class="service abs" style="left:54px">
      <div class="icon-disc"><div class="icon-art" role="img" aria-label="Film frames illustration"></div></div>
      <h3>EDIT YOUR MOVIE</h3>
      <p>Lorem ipsum dolor sit amet, consectetur adipiscing elit, sed do eiusmod tempor incididunt ut labore et dolore magna aliqua.</p>
    </div>
    <div class="service abs" style="left:316px">
      <div class="icon-disc"><div class="icon-art" role="img" aria-label="Film strip with stars illustration"></div></div>
      <h3>SCREEN YOUR MOVIE</h3>
      <p>Lorem ipsum dolor sit amet, consectetur adipiscing elit, sed do eiusmod tempor incididunt ut labore et dolore magna aliqua.</p>
    </div>
    <div class="service abs" style="left:577px">
      <div class="icon-disc"><div class="icon-art" role="img" aria-label="Film and disk illustration"></div></div>
      <h3>CONVERT &amp; TRANSCODE</h3>
      <p>Lorem ipsum dolor sit amet, consectetur adipiscing elit, sed do eiusmod tempor incididunt ut labore et dolore magna aliqua.</p>
    </div>
  </section>

  <h2 class="section-title interface-title abs">Interface Screens</h2>
  <h3 class="interface-heading abs">QUIS NOSTRUD EXERCITATION</h3>
  <p class="interface-text abs">Lorem ipsum dolor sit amet, consectetur adipiscing elit, sed do eiusmod tempor incididunt ut labore et dolore magna aliqua. Ut enim ad minim veniam, quis nostrud exercitation ullamco laboris nisi ut aliquip ex ea commodo consequat. Lorem ipsum dolor</p>
  <a class="btn interface-btn abs" href="#">Learn More</a>
  <div class="screen screen-media abs" role="img" aria-label="Screenshot of the media library interface"></div>
  <div class="screen screen-player abs" role="img" aria-label="Screenshot of the video screening player"></div>

  <footer class="site-footer abs">
    <p class="copyright abs">Copyright ©2015, Yoursite. All Right Reserved.</p>
    <div class="social abs" aria-label="Social links"><span></span><span></span><span></span><span></span><span></span></div>
  </footer>
</body>
</html>
```